Visitenkarten VORALUX Automotive
Zielgruppe
Wir sind Zulieferer für den Reifenfachhandel und vertreiben ausschließlich B2B. Zu unserem Produktsortiment zählen Ventile, Gewichte, TPMS, etc. Wir vertreiben KEINE Reifen und Felgen.
Alle Produkte finden Sie unter www.voralux-shop.example oder unter www.voralux-automotive.example
Aufgabenstellung
Das Design soll modern und gut lesbar sein - nicht zu verspielt.
Die Farben unseres Logos sind:
HKS 41 / Umrechnung in CMYK: 100 Cyan / 70 Magenta / 10 Yellow / 50 Schwarz
RGB : Rot 28 - Grün 49 - Blau 68 / Hexadezimal (WEB) 1C3144
Ich habe auch unser altes Visitenkartendesign als PDF hochgeladen - bei diesem Design stört die Schriftart sehr, da diese sehr schlecht zu lesen ist.

```html
<!DOCTYPE html>
<html lang="de">
<head>
<meta charset="utf-8">
<title>Visitenkarten VORALUX Automotive</title>
<link href="https://fonts.googleapis.com/css2?family=Open+Sans:wght@400;700&display=swap" rel="stylesheet">
<style>
  :root{
    --brand:#1c3f6a;
    --ink:#1a1a1a;
    --paper:#ffffff;
    --stripe:#c4c6c9;
    --stage:#6f6f6f;
  }
  *{margin:0;padding:0;box-sizing:border-box}
  html,body{width:1200px;height:912px;overflow:hidden;background:var(--stage);font-family:"Open Sans",sans-serif}
  .card{position:absolute;width:540px;height:350px;box-shadow:0 6px 18px rgba(0,0,0,.35)}
  .card--front{left:40px;top:140px;background:var(--brand);color:var(--paper)}
  .card--back{left:620px;top:420px;background:var(--paper);color:var(--ink);overflow:hidden}

  .brand-name{font-weight:700;letter-spacing:.02em;white-space:nowrap}
  .card--front .brand-name{position:absolute;left:0;right:0;top:120px;text-align:center;font-size:40px;color:var(--paper)}
  .company-line{position:absolute;left:0;right:0;bottom:42px;text-align:center;font-size:13px;color:var(--paper)}

  .card--back .brand-name{position:absolute;right:34px;top:40px;font-size:28px;color:var(--brand)}
  .person{position:absolute;right:34px;top:108px;text-align:right}
  .person__name{font-size:17px;font-weight:700;color:var(--brand)}
  .person__role{font-size:12px;color:var(--ink)}

  .contact-list{position:absolute;left:30px;top:178px;list-style:none}
  .contact-list li{display:flex;align-items:center;gap:12px;height:21px;font-size:14px}
  .contact-list svg{width:14px;height:14px;fill:var(--brand);flex:none}

  .base-band{position:absolute;left:0;bottom:0;width:540px;height:60px}
</style>
</head>
<body>

<section class="card card--front">
  <div class="brand-name">VORALUX Automotive</div>
  <p class="company-line">VORALUX Automotive GmbH • Lindenweg 7 • 12345 Musterstadt</p>
</section>

<section class="card card--back">
  <div class="brand-name">VORALUX Automotive</div>
  <div class="person">
    <div class="person__name">Markus Teller</div>
    <div class="person__role">Gebietsverkaufsleiter</div>
  </div>

  <ul class="contact-list">
    <li><svg viewBox="0 0 16 16"><path d="M3 1l3 3-2 2c1 2 3 4 5 5l2-2 3 3-2 3C6 15 1 10 1 3z"/></svg>012 34 - 567 89-10</li>
    <li><svg viewBox="0 0 16 16"><path d="M4 1h8v4H4zM1 6h14v7h-3v2H4v-2H1zM5 10v4h6v-4z"/></svg>012 34 - 567 89-16</li>
    <li><svg viewBox="0 0 16 16"><path d="M4 0h8a1 1 0 0 1 1 1v14a1 1 0 0 1-1 1H4a1 1 0 0 1-1-1V1a1 1 0 0 1 1-1zm1 2v10h6V2zm3 11a1 1 0 1 0 0 2 1 1 0 0 0 0-2z"/></svg>0150 - 1234 56 78</li>
    <li><svg viewBox="0 0 16 16"><path d="M8 0a8 8 0 1 0 0 16A8 8 0 0 0 8 0zm0 2a6 6 0 0 1 5.6 4H10L8 4 6 6H2.4A6 6 0 0 1 8 2zM2 8h4l2 2 2-2h4a6 6 0 0 1-12 0z"/></svg>www.voralux-shop.example</li>
    <li><svg viewBox="0 0 16 16"><path d="M8 0a8 8 0 1 0 0 16A8 8 0 0 0 8 0zM7 2v4H3a6 6 0 0 1 4-4zm2 0a6 6 0 0 1 4 4H9zM3 9h4v4a6 6 0 0 1-4-4zm6 0h4a6 6 0 0 1-4 4z"/></svg>www.voralux-automotive.example</li>
    <li><svg viewBox="0 0 16 16"><path d="M0 3h16v1L8 9 0 4zm0 3l8 5 8-5v7H0z"/></svg>markus.teller@voralux-automotive.example</li>
  </ul>

  <svg class="base-band" viewBox="0 0 540 60" preserveAspectRatio="none">
    <polygon fill="var(--stripe)" points="0,44 415,44 435,4 540,4 540,12 440,12 420,52 0,52"/>
    <polygon fill="var(--brand)" points="0,52 420,52 440,12 540,12 540,60 0,60"/>
  </svg>
</section>

</body>
</html>
```